Gleam Forge
Fine Auto Detailers
Thanks all for the designs. Feel free to use any color combo you'd like in your designs. The red is good but would be good to see some other ideas. Thanks.
Draft #15 - I like the reflection image of the GF on the business card. It really makes it stand out.
Thanks to all the designers for submitting there ideas so far. Please keep them coming.
Note to all designers. I would like to ask that you leave the address OFF the business card and stationery. This may seem strange but I only need the phone number, email and web site included. Thank you.
To all designers - I have uploaded .AI files for your convenience. Thank you.

```html
<!DOCTYPE html>
<html lang="en">
<head>
<meta charset="utf-8">
<title>Gleam Forge – Business Card</title>
<link href="https://fonts.googleapis.com/css2?family=Michroma&family=Open+Sans:wght@400;600&display=swap" rel="stylesheet">
<style>
  :root {
    --page: #ffffff;
    --silver-light: #dcdddf;
    --silver-mid: #aaacaf;
    --silver-dark: #8a8c8f;
    --brand-red: #c4161c;
    --brand-red-deep: #9a1116;
    --ink-white: #ffffff;
    --ink-grey: #8a8c8f;
    --card-white: #ffffff;
  }
  * { margin: 0; padding: 0; box-sizing: border-box; }
  html, body {
    width: 1200px; height: 420px; overflow: hidden;
    background: var(--page);
  }
  .sheet { position: relative; width: 1200px; height: 420px; }

  .card {
    position: absolute; top: 67px;
    width: 548px; height: 305px; overflow: hidden;
  }

  /* Front */
  .card--front {
    left: 29px;
    background: linear-gradient(135deg, var(--silver-mid) 0%, var(--silver-light) 38%, var(--silver-mid) 68%, var(--silver-dark) 100%);
  }
  .front-mark {
    position: absolute; left: 0; right: 0; top: 30px; height: 170px;
    display: flex; align-items: center; justify-content: center; gap: 22px;
  }
  .front-mark__square { width: 40px; height: 40px; background: var(--brand-red); }
  .front-mark__initials {
    font-family: "Michroma", sans-serif;
    font-size: 120px; line-height: 1;
    color: var(--brand-red);
  }
  .front-name {
    position: absolute; left: 0; right: 0; top: 224px;
    text-align: center;
    font-family: "Michroma", sans-serif;
    font-size: 33px; letter-spacing: 6px; text-transform: uppercase;
    color: var(--brand-red-deep); white-space: nowrap;
  }
  .front-tagline {
    position: absolute; left: 0; right: 0; top: 270px;
    text-align: center;
    font-family: "Open Sans", sans-serif; font-weight: 600;
    font-size: 15px; letter-spacing: 6px; text-transform: uppercase;
    color: var(--ink-white);
  }

  /* Back */
  .card--back {
    left: 629px; width: 564px;
    background: var(--card-white);
  }
  .back-panel {
    position: absolute; left: 0; top: 0; bottom: 0; width: 264px;
    background: linear-gradient(100deg, var(--silver-dark) 0%, var(--silver-light) 45%, var(--silver-mid) 100%);
  }
  .contact { position: absolute; left: 38px; top: 80px; color: var(--ink-white); }
  .contact__name {
    font-family: "Open Sans", sans-serif; font-weight: 600;
    font-size: 28px; line-height: 1; margin-bottom: 30px;
  }
  .contact__line {
    font-family: "Open Sans", sans-serif;
    font-size: 13px; line-height: 20px; white-space: nowrap;
  }
  .back-brand {
    position: absolute; left: 274px; right: 10px; top: 55px;
    text-align: center;
  }
  .back-brand__mark {
    display: flex; align-items: center; justify-content: center; gap: 12px;
    height: 140px;
  }
  .back-brand__square { width: 22px; height: 22px; background: var(--brand-red); }
  .back-brand__initials {
    font-family: "Michroma", sans-serif;
    font-size: 84px; line-height: 1;
    color: var(--brand-red);
  }
  .back-brand__title {
    margin-top: 42px;
    font-family: "Michroma", sans-serif;
    font-size: 16px; letter-spacing: 3px; text-transform: uppercase;
    color: var(--brand-red-deep); white-space: nowrap;
  }
  .back-brand__tagline {
    margin-top: 8px;
    font-family: "Open Sans", sans-serif; font-weight: 600;
    font-size: 10px; letter-spacing: 4px; text-transform: uppercase;
    color: var(--ink-grey); white-space: nowrap;
  }
</style>
</head>
<body>
  <main class="sheet">
    <section class="card card--front">
      <div class="front-mark">
        <span class="front-mark__square"></span>
        <span class="front-mark__initials">GF</span>
      </div>
      <p class="front-name">Gleam Forge</p>
      <p class="front-tagline">Fine Auto Detailers</p>
    </section>

    <section class="card card--back">
      <div class="back-panel"></div>
      <div class="contact">
        <p class="contact__name">Reed Calloway</p>
        <p class="contact__line">cell: (555)201-0148</p>
        <p class="contact__line">email: reed@gleamforge.com</p>
        <p class="contact__line">url: www.gleamforge.com</p>
      </div>
      <div class="back-brand">
        <div class="back-brand__mark">
          <span class="back-brand__square"></span>
          <span class="back-brand__initials">GF</span>
        </div>
        <p class="back-brand__title">Gleam Forge</p>
        <p class="back-brand__tagline">Fine Auto Detailers</p>
      </div>
    </section>
  </main>
</body>
</html>
```